Premium modern eliquids labels 84.5 x 80 mm

I am looking for modern graphics for the labels of a new eliquid line that will have 4 different types of eliquids. It will have a tobacco one (brown colours maybe), a fruity one (bright colours maybe), a minty one (green colours maybe) and a creamy one (beige colours maybe).
I will need one of them to see how the design is, that design will have to be adapted to the other 3 colours of the label.
The brand logo is attached. I also attached a sample of what is mandatory to write on the label, you can change size, place and font of what is written, the only thing that cannot be reduced is the yellow parts. I attach the bottle that we will use.The size of the label is 84.5 x 80 mm (base x height).

Target Market(s)

vapers

Requirements
Must have
• My project must have one of the labels.

```html
<!DOCTYPE html>
<html lang="it">
<head>
<meta charset="utf-8">
<title>Halcyon Tobacco – etichetta 20 ml</title>
<link href="https://fonts.googleapis.com/css2?family=Roboto+Condensed:wght@400;700&family=Roboto:wght@700&family=Montserrat:wght@700;800;900&display=swap" rel="stylesheet">
<style>
  :root {
    --page: #ffffff;
    --brown-deep: #2a1206;
    --brown-mid: #6b2f0b;
    --brown-warm: #8a4414;
    --brown-light: #c77a44;
    --ink: #ffffff;
    --cream: #ece9c6;
    --yellow: #fbc02d;
    --black: #111111;
    --brand-blue: #6cb7e0;
    --edge: #2e2e2e;
  }
  html, body {
    margin: 0;
    width: 1200px;
    height: 1200px;
    overflow: hidden;
    background: var(--page);
  }
  .canvas { position: relative; width: 1200px; height: 1200px; }
  .label {
    position: absolute;
    left: 165px; top: 162px;
    width: 879px; height: 832px;
    overflow: hidden;
    color: var(--ink);
    font-family: "Roboto Condensed", sans-serif;
    background:
      radial-gradient(ellipse 55% 60% at 30% 45%, var(--brown-warm) 0%, transparent 70%),
      radial-gradient(ellipse 40% 50% at 70% 80%, var(--brown-light) 0%, transparent 70%),
      linear-gradient(90deg, var(--brown-mid) 0%, #5a260a 55%, var(--brown-deep) 100%);
    border-left: 5px solid var(--edge);
    box-sizing: border-box;
  }
  .smoke-backdrop { position: absolute; inset: 0; }
  .ingredients, .instructions {
    position: absolute;
    margin: 0;
    font-weight: 700;
    font-size: 24px;
    line-height: 26px;
    letter-spacing: -0.2px;
  }
  .ingredients { left: 23px; top: 23px; width: 220px; }
  .instructions { left: 694px; top: 23px; width: 170px; line-height: 25.5px; }
  .lot-code {
    position: absolute;
    left: 36px; top: 616px;
    transform: rotate(-90deg);
    transform-origin: 0 0;
    white-space: nowrap;
    font-size: 20px;
    font-weight: 400;
    letter-spacing: -0.3px;
  }
  .lot-code b { font-weight: 700; }
  .producer { position: absolute; left: 23px; top: 626px; }
  .producer-head {
    margin: 0;
    font-family: "Montserrat", sans-serif;
    font-weight: 800;
    font-size: 21px;
    line-height: 20px;
    letter-spacing: 0.6px;
  }
  .producer-address {
    margin: 0;
    font-family: "Roboto", sans-serif;
    font-weight: 700;
    font-size: 18.5px;
    line-height: 19.4px;
  }
  .brand {
    position: absolute;
    left: 262px; top: 178px;
    width: 356px;
    display: flex; align-items: center; justify-content: center; gap: 14px;
    font-family: "Montserrat", sans-serif;
    font-weight: 900;
    font-size: 50px;
    letter-spacing: 2px;
    color: var(--brand-blue);
  }
  .brand-dot { width: 18px; height: 18px; border-radius: 50%; background: var(--brand-blue); }
  .leaf-art {
    position: absolute;
    left: 270px; top: 288px;
    width: 340px; height: 294px;
  }
  .flavour-title {
    position: absolute;
    left: 286px; top: 608px;
    width: 306px;
    display: flex; align-items: center; gap: 8px;
    font-weight: 700;
    font-size: 31px;
    color: var(--cream);
  }
  .flavour-title .rule { flex: 1; height: 3px; background: var(--cream); }
  .tagline {
    position: absolute;
    left: 286px; top: 650px; width: 306px;
    text-align: center;
    font-family: "Roboto", sans-serif;
    font-weight: 700; font-size: 17px;
  }
  .volume {
    position: absolute;
    top: 760px;
    font-weight: 700; font-size: 24px;
    width: 140px; text-align: center;
  }
  .volume.center { left: 369px; }
  .volume.side { left: 701px; }
  .disposal { position: absolute; left: 716px; width: 130px; }
  .disposal .bin-tag {
    background: var(--yellow); color: var(--black);
    font-family: "Montserrat", sans-serif; font-weight: 800;
    font-size: 18px; line-height: 16.5px;
    width: 124px; height: 38px; box-sizing: border-box; padding-top: 2px;
    text-align: center; letter-spacing: 0.2px;
  }
  .disposal .part {
    font-family: "Montserrat", sans-serif; font-weight: 700;
    font-size: 14.5px; margin: 6px 0 6px 2px; letter-spacing: 0.3px;
  }
  .disposal .part.flacone { margin-left: 8px; }
  .disposal .code {
    background: var(--yellow); color: var(--black);
    font-family: "Montserrat", sans-serif; font-weight: 900;
    font-size: 23px; line-height: 38px;
    width: 89px; height: 38px; text-align: center; letter-spacing: 1px;
  }
  .disposal.label-part { top: 403px; }
  .disposal.bottle-part { top: 528px; }
  .recycle-icon { position: absolute; left: 706px; top: 682px; width: 62px; height: 62px; }
  .bin-icon { position: absolute; left: 779px; top: 660px; width: 60px; height: 82px; }
</style>
</head>
<body>
<div class="canvas">
  <section class="label">
    <div class="smoke-backdrop" role="img" aria-label="Sfondo di volute di fumo color tabacco"></div>

    <p class="ingredients">INGREDIENTI:<br>GLICOLE<br>PROPILENICO<br>SOSTANZE<br>AROMATIZZANTI</p>

    <div class="lot-code">L.SH20 - <b>001-PES-</b>D.PROD.<b>22-04-2022</b> D.SC.<b>21-04-2024</b></div>

    <div class="producer">
      <p class="producer-head">PRODOTTO<br>E CONFEZIONATO<br>DA Velmora srl</p>
      <p class="producer-address">Via dei Tigli 48<br>10100 Torino<br>P.i.04815162342<br>Tel. +39 011 5550192<br>info@velmora.it</p>
    </div>

    <div class="brand"><span class="brand-dot"></span>HALCYON</div>

    <svg class="leaf-art" viewBox="0 0 340 294" role="img" aria-label="Illustrazione di foglie di tabacco essiccate">
      <defs>
        <radialGradient id="leafTone" cx="50%" cy="45%" r="60%">
          <stop offset="0%" stop-color="#d89a55"/>
          <stop offset="100%" stop-color="#8a4a1c"/>
        </radialGradient>
      </defs>
      <ellipse cx="170" cy="147" rx="166" ry="143" fill="url(#leafTone)" stroke="#ffffff" stroke-width="3"/>
    </svg>

    <div class="flavour-title"><span class="rule"></span>TOBACCO<span class="rule"></span></div>
    <div class="tagline">Premium Eliquid</div>

    <p class="instructions">ISTRUZIONI<br>D’USO:<br>Agitare bene<br>prima<br>dell’utilizzo.<br>Diluire nelle<br>percentuali<br>consigliate<br>sul nostro<br>sito.<br>Conservare in<br>luogo fresco e<br>asciutto</p>

    <div class="disposal label-part">
      <div class="bin-tag">RACCOLTA<br>PLASTICA</div>
      <div class="part">ETICHETTA</div>
      <div class="code">PAP 5</div>
    </div>
    <div class="disposal bottle-part">
      <div class="bin-tag">RACCOLTA<br>PLASTICA</div>
      <div class="part flacone">FLACONE</div>
      <div class="code">PET 1</div>
    </div>

    <svg class="recycle-icon" viewBox="0 0 62 62" role="img" aria-label="Simbolo riciclo">
      <g id="chase-arrow" fill="#ffffff" stroke="#ffffff" stroke-width="4" stroke-linecap="round">
        <line x1="35" y1="13" x2="47" y2="34"/>
        <polygon points="53,45 44.3,39.7 52.9,34.7" stroke-width="1" stroke-linejoin="round"/>
      </g>
      <use href="#chase-arrow" transform="rotate(120 31 35.3)"/>
      <use href="#chase-arrow" transform="rotate(240 31 35.3)"/>
    </svg>

    <svg class="bin-icon" viewBox="0 0 60 82" role="img" aria-label="Simbolo non disperdere nell'ambiente">
      <g fill="#ffffff">
        <circle cx="45" cy="7" r="6"/>
        <path d="M38 16 H53 Q57 16 57 20 V44 H53 V80 H47 V48 H44 V80 H38 V30 L25 31 Q22 31 22 28 Q22 25 25 25 L38 23 Z"/>
        <circle cx="11" cy="38" r="2"/>
        <circle cx="15" cy="43" r="2"/>
        <circle cx="8" cy="44" r="1.6"/>
      </g>
      <path d="M3 50 H29 L25 80 H7 Z" fill="none" stroke="#ffffff" stroke-width="3.5" stroke-linejoin="round"/>
    </svg>

    <div class="volume center">20 ML NET</div>
    <div class="volume side">20 ML NET</div>
  </section>
</div>
</body>
</html>
```